Business Card Design

My company is a health food catering and delivery business. Our colours are a bright turquiose green/blue, black, white and natural brown based beige. I would like the front of my card (working from the outside in; with a turquoise green boarder -quite thick, with a thin black line separating the turquoise boarder from the beige inside the remaining space of the front of the card with my logo in the centre. This should be all that appears on the front.

On the back I would like all the information displayed above on the beige coloured card, with the blurb in the bright turquoise and my contact information in black please. I would like my business name central - Harvest Lantern Kitchen and immediately below with a right alignment - ...Dine with Delight
Below this should follow all that I have displayed above with a left alignment.

Target Market(s)

Cafes, restaurants, individuals, buying agents & super markets

Industry/Entity Type

Catering

Contact Information for Business Card

BACK OF BUSINESS CARD:
Harvest Lantern Kitchen
...Dine with Delight
Deliciously healthy foods - free from gluten, lactose, cane sugar, trans-fat, GMO corn, soy & rice, no artificial flavours, colours or preservatives.
Prepared fresh from locally sourced ingredients, delivered to your door! For individuals, families, corporate, cafes, restaurants & event catering for Toowoomba & surrounds!

PH: 0491 382 907 // orders@harvestlanternkitchen.example
www.harvestlanternkitchen.example
www.social.example/harvestlanternkitchen

Requirements
Must have
• Please supply a modern, easy to read text that will blend nicely with my logo text.
Nice to have
• I really want my business cards to stand out as these will be the template for brochures, menus and website designers to draw inspiration from!
Should not have
• Please do not use Arial, Tahoma or Times Roman text.

```html
<!DOCTYPE html>
<html lang="en">
<head>
<meta charset="utf-8">
<title>Harvest Lantern Kitchen – Business Card</title>
<link rel="stylesheet" href="https://fonts.googleapis.com/css2?family=Questrial&display=swap">
<style>
  :root {
    --turquoise: #5cc3c0;
    --turquoise-dark: #3fb0ad;
    --ink: #1b1b1b;
    --ink-soft: #3a3a3a;
    --beige: #f7efcf;
    --beige-shade: #ede2b8;
    --stage: #ecebe7;
    --card-w: 540px;
    --card-h: 330px;
  }
  * { box-sizing: border-box; margin: 0; padding: 0; }
  html, body {
    width: 1200px; height: 784px; overflow: hidden;
    background: var(--stage);
    font-family: "Questrial", sans-serif;
    color: var(--ink);
  }
  .canvas {
    width: 1200px; height: 784px;
    display: flex; align-items: center; justify-content: center; gap: 40px;
  }
  .card {
    position: relative;
    width: var(--card-w); height: var(--card-h);
    background: var(--beige);
    box-shadow: 0 6px 18px rgba(0,0,0,.12);
    overflow: hidden;
  }

  /* ---------- Back of card ---------- */
  .card-back .chef-watermark {
    position: absolute; left: 150px; top: 40px; width: 110px; height: 200px;
    border-radius: 50px 50px 20px 20px;
    background: linear-gradient(180deg, rgba(0,0,0,.05), rgba(0,0,0,.02));
  }
  .card-back .name-watermark {
    position: absolute; left: 60px; top: 232px;
    font-size: 44px; color: rgba(0,0,0,.06); white-space: nowrap;
  }
  .business-name {
    position: absolute; top: 26px; left: 0; right: 0;
    text-align: center; font-size: 22px; color: var(--turquoise-dark);
  }
  .tagline {
    position: absolute; top: 56px; left: 0; right: 150px;
    text-align: right; font-size: 15px; color: var(--ink);
  }
  .contact-list {
    position: absolute; left: 22px; top: 158px; width: 262px;
    list-style: none; font-size: 11.5px; line-height: 19px; color: var(--ink);
  }
  .contact-list li { display: flex; align-items: center; gap: 6px; white-space: nowrap; }
  .contact-list svg { width: 12px; height: 12px; flex: none; }
  .divider {
    position: absolute; left: 294px; top: 92px; width: 1px; height: 150px;
    background: var(--ink-soft);
  }
  .blurb {
    position: absolute; left: 306px; top: 94px; width: 214px;
    font-size: 11.5px; line-height: 15.5px; color: var(--ink-soft);
  }
  .blurb p + p { margin-top: 12px; }

  /* ---------- Front of card ---------- */
  .card-front .turquoise-frame {
    position: absolute; inset: 14px;
    border: 12px solid var(--turquoise);
  }
  .card-front .ink-rule {
    position: absolute; inset: 30px;
    border: 1.5px solid var(--ink);
  }
  .logo {
    position: absolute; left: 0; right: 0; top: 48px;
    display: flex; flex-direction: column; align-items: center;
  }
  .logo .chef-illustration {
    width: 200px; height: 170px;
    border-radius: 90px 90px 14px 14px;
    background: linear-gradient(180deg, #ffffff 0%, #e4e0d4 100%);
    border: 1px solid rgba(0,0,0,.15);
  }
  .logo .logo-name {
    margin-top: 10px; font-size: 30px; color: var(--ink); white-space: nowrap;
  }
</style>
</head>
<body>
<main class="canvas">

  <section class="card card-back" aria-label="Back of business card">
    <div class="chef-watermark" role="img" aria-label="Faint chef illustration behind the text"></div>
    <div class="name-watermark" aria-hidden="true">Harvest Lantern Kitchen</div>

    <h1 class="business-name">Harvest Lantern Kitchen</h1>
    <p class="tagline">“...Dine with Delight”</p>

    <ul class="contact-list">
      <li>
        <svg viewBox="0 0 12 12" aria-hidden="true"><path d="M3 1l2 2.5-1.2 1.2a6 6 0 0 0 3.5 3.5L8.5 7 11 9l-1.5 2A9 9 0 0 1 1 2.5z" fill="var(--turquoise-dark)"/></svg>
        0491 382 907
      </li>
      <li>
        <svg viewBox="0 0 12 12" aria-hidden="true"><rect x="1" y="2.5" width="10" height="7" rx="1" fill="none" stroke="var(--turquoise-dark)" stroke-width="1.4"/><path d="M1.5 3l4.5 3.5L10.5 3" fill="none" stroke="var(--turquoise-dark)" stroke-width="1.2"/></svg>
        orders@harvestlanternkitchen.example
      </li>
      <li>
        <svg viewBox="0 0 12 12" aria-hidden="true"><circle cx="6" cy="6" r="5" fill="none" stroke="var(--turquoise-dark)" stroke-width="1.3"/><ellipse cx="6" cy="6" rx="2.2" ry="5" fill="none" stroke="var(--turquoise-dark)" stroke-width="1"/><path d="M1 6h10" stroke="var(--turquoise-dark)" stroke-width="1"/></svg>
        www.harvestlanternkitchen.example
      </li>
      <li>
        <svg viewBox="0 0 12 12" aria-hidden="true"><circle cx="6" cy="6" r="5.5" fill="var(--turquoise-dark)"/></svg>
        www.social.example/harvestlanternkitchen
      </li>
    </ul>

    <div class="divider" aria-hidden="true"></div>

    <div class="blurb">
      <p>Deliciously healthy foods - free from gluten, lactose, cane sugar, trans-fat, GMO corn, soy &amp; rice, no artificial flavours, colours or preservatives. Prepared fresh from locally sourced ingredients, delivered to your door!</p>
      <p>For individuals, families, corporate, cafes, restaurants &amp; event catering for Toowoomba &amp; surrounds!</p>
    </div>
  </section>

  <section class="card card-front" aria-label="Front of business card">
    <div class="turquoise-frame" aria-hidden="true"></div>
    <div class="ink-rule" aria-hidden="true"></div>
    <div class="logo">
      <div class="chef-illustration" role="img" aria-label="Line illustration of a chef in a hat and apron holding a whisk and a frying pan"></div>
      <div class="logo-name">Harvest Lantern Kitchen</div>
    </div>
  </section>

</main>
</body>
</html>
```